New CRM Software Needs an Awesome Banner Ad Campaign Design

Design of digital ads for sizes needed for LinkedIn and Google Remarketing.

Same design will be needed in various sizes (see attached word document for details and instructions).

We need an ad set design promoting a new cloud-based CRM (Customer Relationship Management) software. https://www.brightledgerhub.example/
We are looking for eye-catching, WOW designs, something attractive, but keep it professional. It should also convey quality, security and trust.
Updates

Project Deadline Extended Reason: I am extending the deadline in hopes to get more designers to submit. You need only to submit your design concept in one size. If I choose your design, then you can make the rest of the sizes.Thank you to all who have already submitted! Added Monday, January 16, 2017

Target Market(s)

B2B Audience –Mortgage and bank industries

Industry/Entity Type

Business Software

Font styles to use
Other font styles liked:
• Universe Condensed

Requirements
Must have
• Only one design concept in one size is needed initially, once you are awarded with the project, you can make the other sizes as specified and required.
• Please see attached word document for details and instructions.
• Must have both logos attached as well as use our colors and a modern image appealing to mortgage and banking executives.
Nice to have
Should not have
• Should not have a whole bunch of words and no pictures.

```html
<!DOCTYPE html>
<html lang="en">
<head>
<meta charset="utf-8">
<title>BrightLedger Hub – Banner</title>
<link rel="stylesheet" href="https://fonts.googleapis.com/css2?family=Oswald:wght@500&display=swap">
<style>
  :root {
    --banner-bg: #4d7489;
    --banner-ink: #e9e9e9;
    --button-bg: #ffffff;
    --button-ink: #4d7489;
  }
  html, body {
    margin: 0;
    padding: 0;
    width: 1200px;
    height: 426px;
    overflow: hidden;
    background: var(--banner-bg);
  }
  .banner {
    display: block;
    width: 1200px;
    height: 426px;
    font-family: "Oswald", "Arial Narrow", sans-serif;
    font-weight: 500;
  }
  .brand-name,
  .brand-domain,
  .tagline {
    fill: var(--banner-ink);
  }
  .brand-rule {
    stroke: var(--banner-ink);
    stroke-width: 1.5;
  }
  .cta-box {
    fill: var(--button-bg);
  }
  .cta-label {
    fill: var(--button-ink);
  }
</style>
</head>
<body>
<svg class="banner" viewBox="0 0 1200 426" xmlns="http://www.w3.org/2000/svg" role="img" aria-label="BrightLedger Hub banner: easy to use marketing CRM, request a demo">
  <rect width="1200" height="426" fill="var(--banner-bg)"/>

  <a href="https://www.brightledgerhub.example/">
    <text class="brand-name" x="317" y="162" font-size="122"
          textLength="564" lengthAdjust="spacingAndGlyphs">BRIGHTLEDGER</text>
    <line class="brand-rule" x1="317" y1="184" x2="881" y2="184"/>
    <text class="brand-domain" x="317" y="249" font-size="54"
          textLength="564" lengthAdjust="spacing">HUB.EXAMPLE</text>
  </a>

  <text class="tagline" x="314" y="301" font-size="33"
        textLength="566" lengthAdjust="spacing">EASY TO USE MARKETING CRM</text>

  <a href="https://www.brightledgerhub.example/">
    <rect class="cta-box" x="310" y="322" width="577" height="50"/>
    <text class="cta-label" x="601" y="356" font-size="25" text-anchor="middle"
          letter-spacing="6">REQUEST A DEMO</text>
  </a>
</svg>
</body>
</html>
```